Wex2Legal Letterhead

Need a new letterhead for my law firm.
IDENTIFYING INFORMATION BELOW:
Teodoro R Galvani III
Attorney at Law
Address: 2834 Brackett Ave, Ste 300, Dallas, TX 75204
Phone: 877-642-7183
Fax: 469-538-2716
Email: ted@wex2legal-example.com
Website: www.wex2legal-example.com

Colors
0054AA
0677BA
7BADD7
CADEEF
E8F1F8

Requirements
Must have
• Logo needs to be on the letterhead, along with identifying information which is included in the project description.

```html
<!DOCTYPE html>
<html lang="en">
<head>
<meta charset="utf-8">
<title>Wex2Legal Letterhead</title>
<link rel="stylesheet" href="https://fonts.googleapis.com/css2?family=Roboto:wght@400;500&family=Montserrat:wght@300&family=Libre+Baskerville&display=swap">
<style>
  :root {
    --backdrop: #e6e6e3;
    --paper: #ffffff;
    --ink: #111111;
    --muted: #6e6e6e;
    --band: #07080a;
    --accent: #0677BA;
    --accent-light: #7BADD7;
    --on-band: #ffffff;
  }
  * { margin: 0; padding: 0; box-sizing: border-box; }
  html, body { width: 1200px; height: 1000px; overflow: hidden; background: var(--backdrop); }
  body { position: relative; font-family: "Roboto", Arial, sans-serif; color: var(--ink); }

  .sheet {
    position: absolute; left: 229px; top: 20px; width: 742px; height: 960px;
    background: var(--paper); box-shadow: 0 2px 8px rgba(0,0,0,.18);
  }

  .masthead { position: absolute; top: 44px; left: 0; right: 0; text-align: center; }
  .firm-name { font-family: "Roboto", Arial, sans-serif; font-weight: 500; line-height: 1; letter-spacing: 0; }
  .masthead .firm-name { font-size: 42px; color: var(--ink); }
  .tagline { font-family: "Montserrat", Arial, sans-serif; font-weight: 300; letter-spacing: 3px; line-height: 1; }
  .masthead .tagline { margin-top: 8px; font-size: 17px; color: var(--ink); }
  .attorney-name { margin-top: 24px; font-family: "Libre Baskerville", Georgia, serif; font-size: 13px; color: var(--muted); }
  .attorney-role { margin-top: 10px; font-size: 11px; letter-spacing: 3.5px; color: #444; }
  .masthead-rule { width: 202px; height: 1.5px; background: var(--ink); margin: 11px auto 0; }

  .letter { position: absolute; left: 44px; font-size: 11px; line-height: 1.35; }
  .salutation { top: 276px; }
  .closing { top: 664px; }
  .signature { position: absolute; left: 44px; top: 697px; width: 112px; height: 34px;
    background: linear-gradient(90deg, #d9d9d9, #f0f0f0); border-radius: 3px; }
  .signoff { top: 752px; }
  .signoff .role { font-weight: 500; }

  .footer-band { position: absolute; left: 0; bottom: 0; width: 742px; height: 132px; }
  .footer-band svg.band-shape { position: absolute; inset: 0; }
  .contact { position: absolute; color: var(--on-band); font-size: 11px; display: flex; align-items: center; gap: 7px; }
  .contact svg { width: 11px; height: 11px; flex: none; }
  .contact .divider { width: 1.5px; height: 14px; background: var(--accent); }
  .address { position: absolute; left: 70px; top: 71px; color: var(--on-band); font-size: 11px; }
  .footer-brand { position: absolute; left: 480px; top: 34px; width: 220px; text-align: center; color: var(--on-band); }
  .footer-brand .firm-name { font-size: 30px; }
  .footer-brand .tagline { margin-top: 6px; font-size: 12px; }
</style>
</head>
<body>
  <main class="sheet">
    <header class="masthead">
      <div class="firm-name">Wex2Legal</div>
      <div class="tagline">STEADY COUNSEL</div>
      <div class="attorney-name">TEODORO R GALVANI III</div>
      <div class="attorney-role">ATTORNEY AT LAW</div>
      <div class="masthead-rule"></div>
    </header>

    <p class="letter salutation">Dear Mr. Name Surname</p>
    <p class="letter closing">Sincerely,</p>
    <div class="signature" role="img" aria-label="Handwritten signature of Teodoro"></div>
    <p class="letter signoff">Teodoro R. Galvani<br><span class="role">Attorney at Law</span></p>

    <footer class="footer-band">
      <svg class="band-shape" width="742" height="132" viewBox="0 0 742 132">
        <polygon points="34,0 708,0 742,24 742,132 0,132 0,24" fill="var(--band)"/>
      </svg>

      <div class="contact" style="left:70px; top:24px;">
        <svg viewBox="0 0 12 12"><rect width="12" height="12" rx="2" fill="var(--accent)"/><path d="M3.5 2.5 L5 4.5 L4.3 5.4 Q5.2 7 6.6 7.7 L7.5 7 L9.5 8.5 L8.7 9.7 Q5.5 9.6 2.4 3.4 Z" fill="#fff"/></svg>
        <span class="divider"></span><span>877-642-7183</span>
      </div>
      <div class="contact" style="left:70px; top:43px;">
        <svg viewBox="0 0 12 12"><rect width="12" height="12" rx="2" fill="var(--accent)"/><path d="M2.5 3 H9.5 V7.5 H5 L3 9.5 V7.5 H2.5 Z" fill="#fff"/></svg>
        <span class="divider"></span><span>ted@wex2legal-example.com</span>
      </div>
      <div class="contact" style="left:270px; top:24px;">
        <svg viewBox="0 0 12 12"><rect x="3" y="1" width="6" height="3" fill="var(--accent)"/><rect x="1" y="4" width="10" height="5" rx="1" fill="var(--accent)"/><rect x="3" y="7" width="6" height="4" fill="var(--accent-light)"/></svg>
        <span class="divider"></span><span>469-538-2716</span>
      </div>
      <div class="contact" style="left:270px; top:43px;">
        <svg viewBox="0 0 12 12"><circle cx="6" cy="6" r="5" fill="var(--accent)"/><path d="M1 6 H11 M6 1 V11 M6 1 Q2.8 6 6 11 M6 1 Q9.2 6 6 11" stroke="#fff" stroke-width=".8" fill="none"/></svg>
        <span class="divider"></span><span>www.wex2legal-example.com</span>
      </div>
      <p class="address">2834 Brackett Ave, Ste 300, Dallas, TX 75204</p>

      <div class="footer-brand">
        <div class="firm-name">Wex2Legal</div>
        <div class="tagline">STEADY COUNSEL</div>
      </div>
    </footer>
  </main>
</body>
</html>
```